Psychotherapist's business card

I need a business card design for a psychotherapist. I expect business card to have "light" design. By this I mean that it can somehow translate easiness, serenity. Maybe pastel colours can help you here. I have attached some pictures from Greece. Perhaps they can inspire you to combine colours and to achieve that "light" design.
Updates

Pls, don't use any free samples you may find on business card generators. It looks too simple, uncreative and waste of time! READ size and colour requirements! I don't want to see any shapes like rings, triangles etc.

Contact Information for Business Card

Size: 65mmX60mm

Name - Мирослав Гречихин

Психолог
+7(916)482-39-07
grechikhin.com

I suppose that thin font can look good but it's up to you

Requirements
Must have
• size requirements
Nice to have
• pastel colours
• thin font
Should not have
• black and dark colours
• lines, free design samples used from other web-sites

```html
<!DOCTYPE html>
<html lang="en">
<head>
<meta charset="utf-8">
<title>Business Card – Psychologist</title>
<link href="https://fonts.googleapis.com/css2?family=Questrial&display=swap" rel="stylesheet">
<style>
  :root {
    --backdrop: #000000;
    --card: #ffffff;
    --mint: #87cec5;
    --sun: #fecd45;
    --text-light: #ffffff;
  }
  html, body {
    margin: 0;
    padding: 0;
    width: 1200px;
    height: 999px;
    overflow: hidden;
    background: var(--backdrop);
    font-family: "Questrial", sans-serif;
  }
  .card {
    position: absolute;
    left: 216px;
    top: 145px;
    width: 768px;
    height: 708px;
    background: var(--card);
    overflow: hidden;
  }
  .card__wave {
    position: absolute;
    left: 0;
    top: 0;
    width: 768px;
    height: 708px;
  }
  .emblem {
    position: absolute;
    left: 281px;
    top: 83px;
    width: 186px;
    height: 207px;
    border-radius: 46% 46% 20% 20%;
    background: radial-gradient(circle at 50% 35%, #fde08a 0%, #b9e2dc 55%, #e4f4f1 100%);
  }
  .title {
    position: absolute;
    left: 0;
    width: 768px;
    top: 284px;
    margin: 0;
    text-align: center;
    font-size: 59px;
    font-weight: 400;
    color: var(--mint);
    letter-spacing: 0.5px;
  }
  .person {
    position: absolute;
    left: 43px;
    top: 497px;
    margin: 0;
    font-size: 35px;
    font-weight: 400;
    color: var(--text-light);
  }
  .contacts {
    position: absolute;
    left: 50px;
    top: 574px;
    margin: 0;
    padding: 0;
    list-style: none;
  }
  .contacts__item {
    display: flex;
    align-items: center;
    height: 49px;
    font-size: 29px;
    color: var(--text-light);
  }
  .contacts__icon {
    width: 28px;
    height: 28px;
    margin-right: 37px;
    flex-shrink: 0;
  }
</style>
</head>
<body>
  <div class="card">
    <svg class="card__wave" viewBox="0 0 768 708" aria-hidden="true">
      <path d="M310 457 Q 560 457 768 402 L768 428 Q 600 462 310 459 Z" fill="var(--sun)"/>
      <path d="M0 428 Q 330 498 768 430 L768 708 L0 708 Z" fill="var(--mint)"/>
    </svg>

    <div class="emblem" role="img" aria-label="Tree emblem with spiral crown and spreading roots in mint and yellow"></div>
    <h1 class="title">PSYCHOLOGIST</h1>

    <p class="person">Miroslav Grechikhin</p>
    <ul class="contacts">
      <li class="contacts__item">
        <svg class="contacts__icon" viewBox="0 0 28 28" aria-hidden="true">
          <path d="M6 4 L10 4 L12 10 L9 12 Q11 17 16 19 L18 16 L24 18 L24 22 Q22 25 18 24 Q7 21 4 10 Q3 6 6 4 Z" fill="var(--text-light)"/>
          <path d="M16 3 Q24 4 25 12" stroke="var(--text-light)" stroke-width="2" fill="none"/>
          <path d="M16 8 Q20 9 20.5 12" stroke="var(--text-light)" stroke-width="2" fill="none"/>
        </svg>
        <span>+7(916)482-39-07</span>
      </li>
      <li class="contacts__item">
        <svg class="contacts__icon" viewBox="0 0 28 28" aria-hidden="true">
          <rect x="0" y="0" width="28" height="28" rx="5" fill="var(--text-light)"/>
          <text x="14" y="20" text-anchor="middle" font-family="Questrial, sans-serif" font-size="17" fill="var(--mint)">@</text>
        </svg>
        <span>grechikhin.com</span>
      </li>
    </ul>
  </div>
</body>
</html>
```